MOSLEN Environmental needs an upgrade to its current business cards design

We need an upgrade to our current business cards design, where the MOSLEN acronym is included, as possible and not being overloaded.
MOSLEN Environmental is an Environmental Consultancy Firm based in Sydney.
We would like to see creative designs different from the standard type of business cards (for example, rounded edges, different to standard size of common business cards.

Target Market(s)

industrial companies (oil & gas, petrochemical, mining, insolvency, finance and manufacturing), developers, architect firms, law firms.

Industry/Entity Type

Business

Contact Information for Business Card

logos (brand and acronym), if they don't appear overloaded.
name
role
name of company (MOSLEN Environmental),
address (Level 3, Suite 3C, 47-49 Dorrigan Lane, Wexmoor, NSW, 2188) landline (02 7314 2986)
mobile (staff member)
email (staff member) and
website (www.moslengreen.example).
Include: Contaminated Land, Site Remediation, Groundwater Assessment, Health and Ecological Risk Assessments, Acid Sulfate Soils, Waste Classification.

Font styles to use
Serif
Sans Serif

Requirements
Must have
• A creative design different to the standard type of business cards.
Nice to have
• Rounded edges
• Different size of business cards rather than the standard size.
Should not have
• Preferable not to use white colour background, unless it is required from a creative design proposed.
• Not an overloaded design.
• Avoid black colours

```html
<!DOCTYPE html>
<html lang="en">
<head>
<meta charset="utf-8">
<title>MOSLEN Environmental – Business Card</title>
<link href="https://fonts.googleapis.com/css2?family=Roboto:wght@400;500;700;900&family=Open+Sans:wght@400;600;700&display=swap" rel="stylesheet">
<style>
  :root {
    --bg: #e9e6df;
    --card: #ffffff;
    --green: #7cc242;
    --green-dark: #5aa02c;
    --slate: #4d5152;
    --slate-dark: #3a3d3e;
    --text: #2f3233;
    --shadow: rgba(40, 35, 25, 0.25);
  }
  * { margin: 0; padding: 0; box-sizing: border-box; }
  html, body { width: 1200px; height: 900px; overflow: hidden; background: var(--bg); }
  .canvas { position: relative; width: 1200px; height: 900px; }

  .card {
    position: absolute;
    left: 280px;
    width: 640px;
    height: 370px;
    background: var(--card);
    border-radius: 26px;
    box-shadow: 0 6px 0 #d9d9d9, 0 14px 28px var(--shadow);
    overflow: hidden;
    font-family: "Open Sans", sans-serif;
    color: var(--text);
  }
  .card--front { top: 60px; }
  .card--back { top: 470px; }

  /* Front */
  .brand {
    position: absolute; right: 52px; top: 44px;
    font-family: "Roboto", sans-serif; font-weight: 700;
    color: var(--slate); text-align: right; line-height: 1;
  }
  .brand__name { font-size: 58px; letter-spacing: 1px; }
  .brand__sub { font-size: 17px; letter-spacing: 4.5px; margin-top: 6px; }

  .person { position: absolute; left: 48px; top: 178px; display: flex; align-items: center; gap: 12px; }
  .person__mark { width: 26px; height: 26px; border-radius: 50%; background: var(--green); flex: none; }
  .person__name { font-family: "Roboto", sans-serif; font-weight: 700; font-size: 28px; color: var(--slate); letter-spacing: 0.5px; line-height: 1; }
  .person__role { font-family: "Roboto", sans-serif; font-weight: 500; font-size: 13.5px; color: var(--green); margin-top: 5px; letter-spacing: 0.3px; }

  .contacts { position: absolute; right: 52px; top: 160px; list-style: none; font-size: 14px; line-height: 1.55; }
  .contacts li { display: flex; align-items: center; gap: 8px; }
  .contacts svg { width: 14px; height: 14px; flex: none; }

  .address { position: absolute; left: 86px; bottom: 44px; font-size: 14px; line-height: 1.5; }

  /* Back */
  .acronym { position: absolute; left: 44px; top: 34px; list-style: none; }
  .acronym li { display: flex; align-items: baseline; height: 34px; }
  .acronym__letter { width: 34px; font-family: "Roboto", sans-serif; font-weight: 900; font-size: 32px; color: var(--green); line-height: 1; }
  .acronym__word { font-family: "Roboto", sans-serif; font-weight: 700; font-size: 15px; color: var(--slate); letter-spacing: 0.6px; text-transform: uppercase; }

  .swoosh { position: absolute; inset: 0; width: 100%; height: 100%; }

  .services { position: absolute; right: 44px; bottom: 34px; list-style: none; text-align: right; color: #fff; font-size: 16px; line-height: 1.62; letter-spacing: 0.3px; }
  .services li { display: flex; justify-content: flex-end; align-items: center; gap: 10px; }
  .services svg { width: 13px; height: 13px; flex: none; }
</style>
</head>
<body>
<main class="canvas">

  <section class="card card--front" aria-label="Business card front">
    <div class="brand">
      <div class="brand__name">MOSLEN</div>
      <div class="brand__sub">ENVIRONMENTAL</div>
    </div>

    <div class="person">
      <span class="person__mark"></span>
      <div>
        <div class="person__name">DANIEL ROSWELL</div>
        <div class="person__role">DIRECTOR | PRINCIPAL ENGINEER</div>
      </div>
    </div>

    <ul class="contacts">
      <li><svg viewBox="0 0 14 14"><rect width="14" height="14" rx="3" fill="var(--green)"/><path d="M4 3.5l1.6 0 .7 2-1 .8a5 5 0 0 0 2.4 2.4l.8-1 2 .7v1.6c-3.5.3-6.8-3-6.5-6.5z" fill="#fff"/></svg>+61 273 142 986</li>
      <li><svg viewBox="0 0 14 14"><rect width="14" height="14" rx="3" fill="var(--green)"/><rect x="4.5" y="2.5" width="5" height="9" rx="1" fill="none" stroke="#fff" stroke-width="1.2"/></svg>+61 438 219 067</li>
      <li><svg viewBox="0 0 14 14"><rect width="14" height="14" rx="3" fill="var(--green)"/><rect x="3" y="4" width="8" height="6" fill="none" stroke="#fff" stroke-width="1.1"/><path d="M3 4l4 3 4-3" fill="none" stroke="#fff" stroke-width="1.1"/></svg>daniel@moslengreen.example</li>
      <li><svg viewBox="0 0 14 14"><rect width="14" height="14" rx="3" fill="var(--green)"/><circle cx="7" cy="7" r="3.6" fill="none" stroke="#fff" stroke-width="1.1"/><path d="M3.4 7h7.2M7 3.4c-1.6 2-1.6 5.2 0 7.2M7 3.4c1.6 2 1.6 5.2 0 7.2" fill="none" stroke="#fff" stroke-width="0.8"/></svg>www.moslengreen.example</li>
    </ul>

    <address class="address" style="font-style:normal">
      Level 3, Suite 3C<br>
      47-49 Dorrigan Lane<br>
      Wexmoor NSW 2188
    </address>
  </section>

  <section class="card card--back" aria-label="Business card back">
    <svg class="swoosh" viewBox="0 0 640 370" preserveAspectRatio="none" aria-hidden="true">
      <defs>
        <linearGradient id="swooshFill" x1="0" y1="1" x2="1" y2="0">
          <stop offset="0" stop-color="var(--slate-dark)"/>
          <stop offset="0.55" stop-color="#5f8f3a"/>
          <stop offset="1" stop-color="var(--green)"/>
        </linearGradient>
      </defs>
      <path d="M0 370 L0 300 C 140 300, 330 230, 440 140 C 520 75, 590 40, 640 30 L640 370 Z" fill="url(#swooshFill)"/>
    </svg>

    <ul class="acronym">
      <li><span class="acronym__letter">M</span><span class="acronym__word">onitoring</span></li>
      <li><span class="acronym__letter">O</span><span class="acronym__word">f</span></li>
      <li><span class="acronym__letter">S</span><span class="acronym__word">oil</span></li>
      <li><span class="acronym__letter">L</span><span class="acronym__word">and (and)</span></li>
      <li><span class="acronym__letter">E</span><span class="acronym__word">nvironmental</span></li>
      <li><span class="acronym__letter">N</span><span class="acronym__word">eeds</span></li>
    </ul>

    <ul class="services">
      <li>Contaminated Land<svg viewBox="0 0 13 13"><circle cx="6.5" cy="6.5" r="6.5" fill="#fff"/></svg></li>
      <li>Site Remediation<svg viewBox="0 0 13 13"><circle cx="6.5" cy="6.5" r="6.5" fill="#fff"/></svg></li>
      <li>Groundwater Assessment<svg viewBox="0 0 13 13"><circle cx="6.5" cy="6.5" r="6.5" fill="#fff"/></svg></li>
      <li>Health Risk Assessments<svg viewBox="0 0 13 13"><circle cx="6.5" cy="6.5" r="6.5" fill="#fff"/></svg></li>
      <li>Acid Sulfate Soils<svg viewBox="0 0 13 13"><circle cx="6.5" cy="6.5" r="6.5" fill="#fff"/></svg></li>
      <li>Waste Classification<svg viewBox="0 0 13 13"><circle cx="6.5" cy="6.5" r="6.5" fill="#fff"/></svg></li>
    </ul>
  </section>

</main>
</body>
</html>
```